New business card for civil engineering company - "Keystone Audit"

We need a business card designed for our new structural engineering company.

The company name is "Keystone Audit" logo files attached.

We would like the following:
* Two-sided card
* Simple design

Information to be placed on the card:
Name - Marcus Dellow
Job Title - Director / Structural Engineer
Credentials - BEng(Hons), CPEng, CMengNZ, IntPE(NZ)
Email - marcus.dellow@keystoneaudit.co.nz
mobile - 0219364058
website - www.keystoneaudit.co.nz

```html
<!DOCTYPE html>
<html lang="en">
<head>
<meta charset="utf-8">
<title>Keystone Audit – Business Card</title>
<link href="https://fonts.googleapis.com/css2?family=Exo+2:ital,wght@0,400;0,500;0,700;1,400&display=swap" rel="stylesheet">
<style>
  :root {
    --backdrop: #b4b4b4;
    --navy: #1d375a;
    --card-white: #f4f4f3;
    --ink-dark: #2b2b2b;
    --ink-grey: #555;
    --accent-blue: #3f6fb0;
    --rule-blue: #5d8fcf;
    --tagline-light: #c9d6e6;
  }
  * { margin: 0; padding: 0; box-sizing: border-box; }
  html, body { width: 1200px; height: 576px; overflow: hidden; }
  body {
    background: var(--backdrop);
    font-family: "Exo 2", sans-serif;
    position: relative;
  }
  .card {
    position: absolute;
    top: 138px;
    width: 484px;
    height: 293px;
    overflow: hidden;
    box-shadow: 2px 3px 5px rgba(0,0,0,0.3);
  }
  .card-front { left: 81px; background: var(--navy); }
  .card-back  { left: 602px; background: var(--card-white); }

  .brand-name {
    position: absolute;
    font-weight: 500;
    letter-spacing: 1.5px;
    white-space: nowrap;
  }
  .brand-tagline {
    position: absolute;
    font-size: 8.5px;
    letter-spacing: 1.6px;
    white-space: nowrap;
  }
  .card-front .brand-name {
    left: 0; right: 0; top: 198px;
    text-align: center;
    font-size: 20px;
    color: #fff;
  }
  .card-front .brand-tagline {
    left: 0; right: 0; top: 225px;
    text-align: center;
    color: var(--tagline-light);
  }
  .card-back .brand-name {
    right: 24px; top: 157px;
    font-size: 18px;
    color: var(--ink-dark);
  }
  .card-back .brand-tagline {
    right: 24px; top: 182px;
    color: var(--ink-grey);
  }

  .person-name {
    position: absolute; left: 23px; top: 178px;
    font-size: 21px; font-weight: 700; color: var(--navy);
  }
  .person-title {
    position: absolute; left: 23px; top: 204px;
    font-size: 11.5px; font-style: italic; color: var(--navy);
  }
  .person-credentials {
    position: absolute; left: 23px; top: 220px;
    font-size: 11.5px; color: var(--accent-blue);
  }
  .divider {
    position: absolute; left: 23px; right: 24px; top: 242px;
    height: 1px; background: var(--rule-blue);
  }
  .contact-row {
    position: absolute; left: 23px; right: 24px; top: 255px;
    display: flex; align-items: center; justify-content: space-between;
    font-size: 10.5px; color: var(--navy); white-space: nowrap;
  }
  .contact-row svg { width: 9px; height: 9px; fill: var(--navy); flex: none; }
  .contact-row .item { display: flex; align-items: center; gap: 4px; }
</style>
</head>
<body>
  <section class="card card-front">
    <div class="brand-name">KEYSTONE AUDIT</div>
    <div class="brand-tagline">PEER REVIEW SPECIALISTS</div>
  </section>

  <section class="card card-back">
    <div class="brand-name">KEYSTONE AUDIT</div>
    <div class="brand-tagline">PEER REVIEW SPECIALISTS</div>

    <div class="person-name">Marcus Dellow</div>
    <div class="person-title">Director / Structural Engineer</div>
    <div class="person-credentials">BEng(Hons), CPEng, CMengNZ, IntPE(NZ)</div>
    <div class="divider"></div>

    <div class="contact-row">
      <span class="item">
        <svg viewBox="0 0 10 10" aria-hidden="true"><path d="M1 3 Q5 0 9 3 L8 4.5 L6.5 3.6 L3.5 3.6 L2 4.5 Z M2.5 5 H7.5 L8.5 9 H1.5 Z"/></svg>
        0219364058
      </span>
      <span class="item">
        <svg viewBox="0 0 10 10" aria-hidden="true"><path d="M0.5 2 H9.5 V8 H0.5 Z M1.2 2.6 L5 5.5 L8.8 2.6" fill="var(--navy)" stroke="#fff" stroke-width="0.6"/></svg>
        marcus.dellow@keystoneaudit.co.nz
      </span>
      <span class="item">
        <svg viewBox="0 0 10 10" aria-hidden="true"><circle cx="5" cy="5" r="4.5"/><path d="M0.5 5 H9.5 M5 0.5 V9.5 M5 0.5 Q2 5 5 9.5 M5 0.5 Q8 5 5 9.5" stroke="#fff" stroke-width="0.5" fill="none"/></svg>
        www.keystoneaudit.co.nz
      </span>
    </div>
  </section>
</body>
</html>
```